Postcard Design

I am an attorney in Pittsburgh. Here and across country, companies are sending data with names, address and new criminal charges for people. This has resulted in some people getting 12 or more of these letters. I want to do a postcard because one does not need to open a postcard. I also want to be delicate since there is no sealed envelope. I want to throw in other matters other than criminal so it does not look like the person is necessarily charged with a crime.
At top would be "Law Office of Dorian F. Haslbeck"
Then:
Need an Attorney?
Attorney Dorian F. Haslbeck has 25 Years of Experience
Free Consultation - Affordable Fees - Credit Cards Accepted
-All Criminal Matters
-Most Civil Matters
-DUI / Traffic Citations / License Restoration
412-555-0187
www.lakesidedefenselawyer.example
www.dfhcounsel.example

My CTQ ranking is A+ but I am not sure they give a logo with the rating. I have all my logos at www.lakesidedefenselawyer.example The purpose of the two websites is these are postcards. I want no one to think oh this person is charged with a crime.

Industry/Entity Type

Attorney

```html
<!DOCTYPE html>
<html lang="en">
<head>
<meta charset="utf-8">
<title>Law Office of Dorian F. Haslbeck – Postcard</title>
<link href="https://fonts.googleapis.com/css2?family=Libre+Baskerville:wght@400;700&family=Oswald:wght@500&family=Open+Sans:wght@400;600&display=swap" rel="stylesheet">
<style>
  :root{
    --bg:#f1f1f1;
    --maroon:#5a1414;
    --maroon-dark:#3e0b0b;
    --maroon-mid:#7a2a22;
    --gold:#c9a24a;
    --gold-light:#efdca0;
    --brown-text:#7a5418;
    --ink:#1b1b1b;
    --paper:#ffffff;
    --cream:#f7f3ea;
    --line:#b9b9b9;
  }
  *{box-sizing:border-box;margin:0;padding:0}
  html,body{width:1200px;height:974px;overflow:hidden;background:var(--bg)}
  .canvas{position:relative;width:1200px;height:974px}

  /* ---------- back of postcard ---------- */
  .card-back{position:absolute;left:80px;top:60px;width:690px;height:450px;background:var(--paper);box-shadow:0 2px 8px rgba(0,0,0,.18);overflow:hidden}
  .back-emblem{position:absolute;left:14px;top:14px;width:92px;height:92px;border-radius:50%;border:4px solid var(--maroon);background:radial-gradient(circle at 40% 40%,#e9dcc4,#a8773f)}
  .back-title{position:absolute;left:110px;top:92px;width:250px;text-align:center;font-family:"Libre Baskerville",serif;color:var(--maroon);font-size:19px;line-height:22px}
  .back-band{position:absolute;left:0;top:142px;width:395px;height:48px;background:var(--maroon);color:#fff;text-align:center;padding-top:4px}
  .back-band .experience{font-family:"Open Sans",sans-serif;font-size:13px;font-weight:600}
  .back-band .offer{font-family:"Oswald",sans-serif;font-size:15px;letter-spacing:.3px}
  .back-photo{position:absolute;left:0;top:190px;width:385px;height:222px;background:linear-gradient(135deg,#b8c2c8 0%,#5f6670 35%,#2b2f3a 60%,#1c2236 100%)}
  .back-footer{position:absolute;left:0;top:412px;width:395px;height:38px;background:#0d0d0d;color:#fff;font-family:"Open Sans",sans-serif;font-weight:600;font-size:15px;display:flex;align-items:center;justify-content:space-between;padding:0 14px 0 38px}
  .back-footer .phone{display:flex;align-items:center;gap:6px}
  .divider{position:absolute;left:395px;top:190px;width:1px;height:222px;background:#8a8fb8}
  .stamp-box{position:absolute;left:570px;top:14px;width:82px;height:90px;border:1.5px solid #444}
  .address-line{position:absolute;left:420px;width:240px;height:1px;background:var(--line)}
  .badge{position:absolute;border-radius:50%}
  .badge-round{width:40px;height:40px;background:radial-gradient(circle,#e2c46a 35%,#1f3e7a 38%)}
  .badge-seal{width:42px;height:42px;background:radial-gradient(circle,#f2efe6 40%,#5a1414 44%)}
  .badge-square{position:absolute;width:28px;height:42px;background:#1f5fa8;border-radius:3px}

  /* ---------- front of postcard ---------- */
  .card-front{position:absolute;left:400px;top:470px;width:690px;height:470px;background:var(--cream);box-shadow:0 3px 12px rgba(0,0,0,.25);overflow:hidden}
  .front-header{position:absolute;left:0;top:0;width:690px;height:128px;background:linear-gradient(180deg,#e7dad6 0%,#8d3a33 30%,var(--maroon) 100%)}
  .front-kicker{position:absolute;left:160px;top:44px;width:520px;text-align:center;font-family:"Open Sans",sans-serif;font-weight:600;color:#fff;font-size:17px;letter-spacing:1px}
  .front-title{position:absolute;left:160px;top:70px;width:520px;text-align:center;font-family:"Libre Baskerville",serif;font-weight:700;color:#fff;font-size:25px;text-shadow:0 2px 2px rgba(0,0,0,.45)}
  .gold-rule{position:absolute;left:0;top:128px;width:690px;height:5px;background:linear-gradient(90deg,var(--gold),var(--gold-light),var(--gold))}
  .header-badge{position:absolute;left:30px;top:14px;width:104px;height:104px;border-radius:50%;background:radial-gradient(circle,#f3efe4 48%,#1f2f66 52%,#1f2f66 84%,var(--gold) 88%)}
  .front-body{position:absolute;left:0;top:133px;width:690px;height:182px;background:linear-gradient(180deg,#fbf8f0,#ece3d0)}
  .gold-strip{position:absolute;left:10px;top:133px;width:98px;height:337px;background:linear-gradient(90deg,#b8913e,var(--gold-light),#b8913e)}
  .attorney-photo{position:absolute;left:18px;top:195px;width:96px;height:118px;border:3px solid var(--gold);background:linear-gradient(160deg,#c5cdd6,#8a98a8 50%,#4c5868)}
  .headline{position:absolute;left:120px;top:148px;width:540px;text-align:center;font-family:"Libre Baskerville",serif;font-weight:700;color:var(--brown-text);font-size:44px;line-height:50px}
  .experience-line{position:absolute;left:120px;top:208px;width:540px;text-align:center;font-family:"Libre Baskerville",serif;font-weight:700;color:var(--brown-text);font-size:14px}
  .practice-areas{position:absolute;left:120px;top:230px;width:540px;text-align:center;font-family:"Libre Baskerville",serif;color:var(--ink);font-size:15px;line-height:20px;list-style:none}
  .practice-areas .star{color:var(--maroon);margin:0 6px}
  .front-site{position:absolute;left:120px;top:290px;width:540px;text-align:center;font-family:"Open Sans",sans-serif;font-weight:600;color:var(--ink);font-size:15px}
  .front-contact-area{position:absolute;left:0;top:315px;width:690px;height:155px;background:linear-gradient(180deg,var(--maroon-mid),var(--maroon-dark))}
  .contact-list{position:absolute;left:122px;top:338px;font-family:"Open Sans",sans-serif;color:#fff;font-size:13px;line-height:19px;list-style:none}
  .contact-list b{font-weight:600;display:inline-block;width:56px;font-weight:400}
  .contact-list span{font-weight:600}
  .offer-strip{position:absolute;left:108px;top:425px;width:582px;height:45px;border-top:1px solid var(--gold);font-family:"Open Sans",sans-serif;color:#fff;font-size:16px;display:flex;align-items:center;padding-left:12px;gap:10px}
  .offer-strip .star{color:#fff;font-size:12px}
  .strip-badge{position:absolute;left:34px;top:358px;width:50px;height:50px;border-radius:50%;background:radial-gradient(circle,#e2c46a 35%,#1f3e7a 40%)}
  .gavel{position:absolute;left:508px;top:255px;width:170px;height:175px;background:radial-gradient(ellipse at 50% 80%,#8a4a22 0%,#5e2e12 45%,rgba(94,46,18,0) 72%);border-radius:8px}
</style>
</head>
<body>
<main class="canvas">

  <!-- Back side -->
  <section class="card-back" aria-label="Postcard back">
    <div class="back-emblem" role="img" aria-label="Photo of law books, scales and gavel"></div>
    <h2 class="back-title">Law Office of<br>Dorian F. Haslbeck</h2>
    <div class="back-band">
      <p class="experience">Attorney Dorian F. Haslbeck has 25 Years of Experience</p>
      <p class="offer">FREE CONSULTATION - AFFORDABLE FEES - CREDIT CARDS ACCEPTED</p>
    </div>
    <div class="back-photo" role="img" aria-label="Photo of a police officer writing a citation in a patrol car"></div>
    <div class="back-footer">
      <span class="site">www.dfhcounsel.example</span>
      <span class="phone">
        <svg width="16" height="16" viewBox="0 0 24 24" aria-hidden="true"><circle cx="12" cy="12" r="11" fill="none" stroke="#fff" stroke-width="2"/><path d="M8 6l2 0 1 3-1.5 1a7 7 0 0 0 4 4l1-1.5 3 1 0 2a2 2 0 0 1-2 2A10 10 0 0 1 6 8a2 2 0 0 1 2-2z" fill="#fff"/></svg>
        412-555-0187
      </span>
    </div>
    <div class="divider"></div>
    <div class="stamp-box"></div>
    <div class="address-line" style="top:200px"></div>
    <div class="address-line" style="top:236px"></div>
    <div class="address-line" style="top:272px"></div>
    <div class="address-line" style="top:308px"></div>
    <div class="badge badge-round" style="left:522px;top:368px" role="img" aria-label="Lawyer listing badge"></div>
    <div class="badge badge-seal" style="left:578px;top:367px" role="img" aria-label="Lawyer award seal"></div>
    <div class="badge-square" style="left:636px;top:366px" role="img" aria-label="CTQ rating badge"></div>
  </section>

  <!-- Front side -->
  <section class="card-front" aria-label="Postcard front">
    <div class="front-header"></div>
    <div class="header-badge" role="img" aria-label="Top lawyer award seal"></div>
    <p class="front-kicker">PITTSBURGH CRIMINAL DEFENSE ATTORNEY</p>
    <h1 class="front-title">Law Office of Dorian F. Haslbeck</h1>
    <div class="gold-rule"></div>
    <div class="front-body"></div>
    <div class="front-contact-area"></div>
    <div class="gold-strip"></div>
    <div class="attorney-photo" role="img" aria-label="Photo of the attorney at his desk"></div>
    <h2 class="headline">Need an Attorney?</h2>
    <p class="experience-line">Attorney Dorian F. Haslbeck has 25 Years of Experience</p>
    <ul class="practice-areas">
      <li>All Criminal Matters<span class="star">★</span>Most Civil Matters</li>
      <li>DUI / Traffic Citations / License Restoration</li>
    </ul>
    <p class="front-site">www.lakesidedefenselawyer.example</p>
    <div class="gavel" role="img" aria-label="Illustration of a wooden gavel on a sound block"></div>
    <ul class="contact-list">
      <li><b>Office number:</b> <span>412-555-0187</span></li>
      <li><b>Email:</b> <span>contact@dfhcounsel.example</span></li>
      <li><b>Website:</b> <span>www.dfhcounsel.example</span></li>
    </ul>
    <div class="strip-badge" role="img" aria-label="Lawyer listing badge"></div>
    <p class="offer-strip">Free Consultation <span class="star">★</span> Affordable Fees <span class="star">★</span> Credit Cards Accepted</p>
  </section>

</main>
</body>
</html>
```